TRU PEAK POWER.

I'd like my business logo.
contact name: Desmond Halvik
phone:0438275160
email: info@trupeakpower.net.au
website: www.trupeakpower.net.au

services:
solar
battery storage
LED lighting
energy saving solutions
general electrical
I'd like the design to look professional

Target Market(s)

Everyone

Industry/Entity Type

Business

Contact Information for Business Card

as described above

Requirements
Must have
• Id like the colours and the design to work well with my logo.

```html
<!DOCTYPE html>
<html lang="en">
<head>
<meta charset="utf-8">
<title>Tru Peak Power – Business Card</title>
<link rel="stylesheet" href="https://fonts.googleapis.com/css2?family=Oswald:wght@300;400;500&display=swap">
<style>
  :root {
    --stage: #d9d9d9;
    --card-white: #f7f7f5;
    --leaf-green: #7db83a;
    --ink: #1c1c1c;
    --sun-orange: #f0940f;
    --paper-white: #ffffff;
  }
  html, body {
    margin: 0;
    padding: 0;
    width: 1200px;
    height: 800px;
    overflow: hidden;
    background: var(--stage);
  }
  .business-card {
    position: absolute;
    left: 100px;
    top: 110px;
    width: 1000px;
    height: 580px;
    filter: drop-shadow(0 12px 24px rgba(0,0,0,0.18));
  }
  .card-base { fill: var(--card-white); }
  .green-panel { fill: var(--leaf-green); }
  .green-arc { fill: none; stroke: var(--leaf-green); stroke-width: 9; }
  .services-band { fill: var(--card-white); }
  .divider-line { stroke: var(--paper-white); stroke-width: 3; }
  .holder-name {
    font-family: 'Oswald', sans-serif;
    font-weight: 500;
    font-size: 58px;
    fill: var(--ink);
  }
  .contact-line {
    font-family: 'Oswald', sans-serif;
    font-weight: 300;
    font-size: 24px;
    fill: var(--paper-white);
  }
  .contact-icon { fill: none; stroke: var(--ink); stroke-width: 2.5; stroke-linejoin: round; stroke-linecap: round; }
  .services-line {
    font-family: 'Oswald', sans-serif;
    font-weight: 400;
    font-size: 31px;
    fill: var(--sun-orange);
  }
  .brand-name {
    font-family: 'Oswald', sans-serif;
    font-weight: 500;
    font-size: 34px;
    fill: var(--leaf-green);
  }
  .brand-dot { fill: var(--sun-orange); }
</style>
</head>
<body>
<svg class="business-card" viewBox="0 0 1000 580" xmlns="http://www.w3.org/2000/svg">
  <defs>
    <clipPath id="card-shape">
      <rect x="0" y="0" width="1000" height="580" rx="48" ry="48"/>
    </clipPath>
  </defs>
  <g clip-path="url(#card-shape)">
    <rect class="card-base" x="0" y="0" width="1000" height="580"/>
    <path class="green-panel" d="M0,0 H500 C610,120 660,320 615,580 H0 Z"/>
    <path class="green-arc" d="M528,0 C640,120 690,320 645,580"/>
    <rect class="services-band" x="0" y="470" width="1000" height="62"/>
    <line class="divider-line" x1="0" y1="258" x2="470" y2="258"/>
  </g>

  <text class="holder-name" x="450" y="230" text-anchor="end">DESMOND HALVIK</text>

  <text class="contact-line" x="450" y="305" text-anchor="end">0438275160</text>
  <text class="contact-line" x="450" y="355" text-anchor="end">WWW.TRUPEAKPOWER.NET.AU</text>
  <text class="contact-line" x="450" y="405" text-anchor="end">INFO@TRUPEAKPOWER.NET.AU</text>

  <g class="contact-icon">
    <circle cx="490" cy="296" r="17"/>
    <path d="M483,287 l4,-2 l3,6 l-3,2 q2,5 6,8 l2,-3 l6,3 l-2,4 q-10,1 -16,-18 z"/>
  </g>
  <g class="contact-icon">
    <circle cx="490" cy="346" r="17"/>
    <ellipse cx="490" cy="346" rx="7" ry="17"/>
    <line x1="473" y1="346" x2="507" y2="346"/>
  </g>
  <g class="contact-icon">
    <rect x="473" y="384" width="34" height="24"/>
    <path d="M473,384 L490,398 L507,384"/>
  </g>

  <circle class="brand-dot" cx="712" cy="238" r="14"/>
  <text class="brand-name" x="736" y="250">TRU PEAK POWER</text>

  <text class="services-line" x="30" y="514">SOLAR • BATTERY STORAGE • LED LIGHTING • ENERGY SAVING SOLUTIONS</text>
</svg>
</body>
</html>
```